New Packaging Design Project

Wine packaging redesign. Retail partner requested a redesign of a private label wine. The old label is attached. Our partner liked the Lantern and Briar label and wanted something similar. There will be a logo added to the top of the label

Went on vacation/holiday

```html
<!DOCTYPE html>
<html lang="en">
<head>
<meta charset="utf-8">
<title>Red Blend 2018 Label</title>
<link rel="stylesheet" href="https://fonts.googleapis.com/css2?family=Big+Shoulders+Display:wght@300&family=Oswald:wght@300;400;600&display=swap">
<style>
  :root {
    --gold: #dbaf66;
    --slate: #878785;
    --taupe: #bab3ad;
    --mist: #d6d8d5;
    --white: #ffffff;
    --pale: #dcdcdc;
    --cream: #f1ece4;
  }
  html, body {
    margin: 0;
    padding: 0;
    width: 683px;
    height: 1200px;
    overflow: hidden;
    background: var(--slate);
  }
  .label {
    position: relative;
    width: 683px;
    height: 1200px;
    overflow: hidden;
    background: linear-gradient(to bottom, var(--gold) 0, var(--gold) 320px, var(--slate) 860px, var(--slate) 100%);
  }
  .region-title {
    position: absolute;
    top: 118px;
    left: 0;
    width: 100%;
    margin: 0;
    text-align: center;
    white-space: nowrap;
    font-family: "Big Shoulders Display", sans-serif;
    font-weight: 300;
    font-size: 136px;
    line-height: 1;
    letter-spacing: 3px;
    color: var(--white);
    z-index: 2;
  }
  .landscape {
    position: absolute;
    top: 320px;
    left: 0;
    width: 683px;
    height: 540px;
    background: linear-gradient(to bottom,
      var(--gold) 0%,
      var(--taupe) 12%,
      var(--taupe) 38%,
      var(--mist) 52%,
      var(--white) 66%,
      var(--white) 76%,
      var(--gold) 88%,
      var(--slate) 100%);
  }
  .contour {
    position: absolute;
    left: 0;
    top: 1100px;
    width: 683px;
    height: 100px;
  }
  .blend-name {
    position: absolute;
    top: 944px;
    left: 0;
    width: 100%;
    margin: 0;
    text-align: center;
    font-family: "Oswald", sans-serif;
    font-weight: 400;
    font-size: 52px;
    line-height: 1;
    letter-spacing: 4px;
    color: var(--gold);
  }
  .varietals {
    position: absolute;
    top: 1020px;
    left: 0;
    width: 100%;
    margin: 0;
    text-align: center;
    font-family: "Oswald", sans-serif;
    font-weight: 300;
    font-size: 25px;
    line-height: 33px;
    letter-spacing: 0.5px;
    color: var(--pale);
  }
  .vintage {
    position: absolute;
    top: 1110px;
    left: 0;
    width: 100%;
    margin: 0;
    text-align: center;
    font-family: "Oswald", sans-serif;
    font-weight: 600;
    font-size: 36px;
    line-height: 1;
    letter-spacing: 3px;
    color: var(--cream);
  }
</style>
</head>
<body>
  <main class="label">
    <h1 class="region-title">NAPA VALLEY</h1>

    <div class="landscape" role="img" aria-label="Stylised valley landscape: a taupe mountain peak, pale grey hills, white mist and golden vineyard rows curving toward the foreground"></div>

    <svg class="contour" viewBox="0 0 683 100" aria-hidden="true">
      <path d="M0 18 C60 50 130 80 220 100" fill="none" stroke="var(--white)" stroke-width="4" stroke-linecap="round"/>
    </svg>

    <h2 class="blend-name">RED BLEND</h2>
    <p class="varietals">
      MERLOT&nbsp;&nbsp;|&nbsp;&nbsp;&nbsp;CABERNET&nbsp; SAUVIGNON<br>
      CABERNET&nbsp; FRANC&nbsp;&nbsp;|&nbsp;&nbsp;&nbsp;PETIT VERDOT&nbsp;&nbsp;|&nbsp;&nbsp;&nbsp;MALBEC
    </p>
    <p class="vintage">2018</p>
  </main>
</body>
</html>
```